Brevolt Solar business cards for carl dunwiddie

Need a solar business card designed. I sell solar systems to home owners. Company’s name is Brevolt solar. I want the business card to have this.
Brevolt Solar
Carl Dunwiddie
210.555.0143
Solar consultant
Cdunwiddie@brevoltsolar.example
I would like the card to be black and green with the brevolt logo on it if possible. If it’s possible to make atleast one of the designs green background with black lettering I would like to see that.
No upfront cost! Start saving today!
Target Market(s)
Residential home owners
Industry/Entity Type
Solar Energy
Contact Information for Business Card
Brevolt Solar
Carl Dunwiddie
210.555.0143
Solar consultant
Cdunwiddie@brevoltsolar.example
Also if it would look better by adding in one of these that would be fine.

```html
<!DOCTYPE html>
<html lang="en">
<head>
<meta charset="utf-8">
<title>Brevolt Solar business cards</title>
<link href="https://fonts.googleapis.com/css2?family=Montserrat:wght@400;500;700&display=swap" rel="stylesheet">
<style>
  :root {
    --stage: #2a2a2a;
    --card: #1b1b1b;
    --card-edge: #101010;
    --green: #6cc24a;
    --green-dim: #3f5a33;
    --white: #e8e8e8;
  }
  * { margin: 0; padding: 0; box-sizing: border-box; }
  html, body { width: 1200px; height: 900px; overflow: hidden; }
  body {
    background: var(--stage);
    font-family: "Montserrat", sans-serif;
    position: relative;
  }
  .card {
    position: absolute;
    width: 560px;
    height: 320px;
    background: var(--card);
    border-radius: 26px;
    box-shadow: 0 6px 0 var(--card-edge), 0 18px 40px rgba(0,0,0,.45);
    overflow: hidden;
  }
  .card--front { left: 120px; top: 110px; }
  .card--back { left: 520px; top: 470px; }

  /* front */
  .front-wordmark {
    position: absolute;
    left: 0; right: 0; top: 118px;
    text-align: center;
    color: var(--green);
    font-weight: 500;
    font-size: 40px;
    letter-spacing: 1px;
  }
  .front-web {
    position: absolute;
    left: 0; right: 0; bottom: 44px;
    text-align: center;
    color: var(--white);
    font-size: 13px;
    letter-spacing: 4px;
  }
  .front-web .accent { color: var(--green); }

  /* back */
  .back-decor {
    position: absolute;
    right: -90px; top: 20px;
    width: 300px; height: 300px;
    border-radius: 50%;
    background: var(--green-dim);
  }
  .back-wordmark {
    position: absolute;
    left: 36px; top: 40px;
    color: var(--green);
    font-weight: 500;
    font-size: 30px;
    letter-spacing: .5px;
  }
  .person { position: absolute; left: 36px; top: 150px; }
  .person__name { color: var(--green); font-weight: 700; font-size: 24px; }
  .person__title { color: var(--white); font-size: 13px; margin-top: 2px; }
  .contacts {
    position: absolute; left: 36px; top: 218px;
    list-style: none;
    color: var(--white);
    font-size: 13px;
  }
  .contacts li { display: flex; align-items: center; gap: 10px; height: 24px; }
  .contacts svg { width: 14px; height: 14px; fill: var(--green); flex: none; }
  .contacts .accent { color: var(--green); }
</style>
</head>
<body>
  <section class="card card--front">
    <div class="front-wordmark">Brevolt Solar</div>
    <div class="front-web">www.<span class="accent">brevoltsolar</span>.example</div>
  </section>

  <section class="card card--back">
    <div class="back-decor"></div>
    <div class="back-wordmark">Brevolt Solar</div>
    <div class="person">
      <div class="person__name">Carl Dunwiddie</div>
      <div class="person__title">Solar consultant</div>
    </div>
    <ul class="contacts">
      <li>
        <svg viewBox="0 0 24 24"><path d="M6.6 10.8a15 15 0 0 0 6.6 6.6l2.2-2.2a1 1 0 0 1 1-.25 11.4 11.4 0 0 0 3.6.57 1 1 0 0 1 1 1V20a1 1 0 0 1-1 1A17 17 0 0 1 3 4a1 1 0 0 1 1-1h3.5a1 1 0 0 1 1 1c0 1.25.2 2.45.57 3.57a1 1 0 0 1-.25 1z"/></svg>
        210.555.0143
      </li>
      <li>
        <svg viewBox="0 0 24 24"><path d="M2 5h20v14H2zm2 2v.5l8 5 8-5V7z"/></svg>
        Cdunwiddie@brevoltsolar.example
      </li>
      <li>
        <svg viewBox="0 0 24 24"><circle cx="12" cy="12" r="10"/></svg>
        <span>www.<span class="accent">brevoltsolar</span>.example</span>
      </li>
    </ul>
  </section>
</body>
</html>
```